Natural Health Supplement Company Needs a Product Label Designed

HARVEST ROOT LABS needs a PROBIOTICS product label designed.We are a natural health vitamin and dietary supplement company. Who ever wins will have the opportunity to design a lot more product labels for us.
Product name: PROBIOTICS
*Please use the attached logo and base the label text exactly off the Kelt Wellness label example.
Other product examples have been attached for inspiration.

Colors

Designer to choose colors to be used in the design.

Requirements
Must have
• Product name: PROBIOTICS
• *Please use the attached logo and base the label text exactly off the Kelt Wellness label example.
• Other product examples have been attached for inspiration.

```html
<!DOCTYPE html>
<html lang="en">
<head>
<meta charset="utf-8">
<title>Floriva-40 Label – Harvest Root Labs</title>
<link rel="stylesheet" href="https://fonts.googleapis.com/css2?family=Roboto+Condensed:wght@400;700&family=Open+Sans:wght@400;700&family=Syncopate:wght@700&family=Archivo+Black&display=swap">
<style>
  :root{
    --teal:#23a093;
    --green:#8dc63f;
    --green-light:#a9d46a;
    --ink:#231f20;
    --white:#fff;
  }
  *{margin:0;padding:0;box-sizing:border-box;}
  html,body{width:1200px;height:445px;overflow:hidden;background:var(--white);}
  .label{position:relative;width:1200px;height:445px;font-family:"Roboto Condensed",sans-serif;color:var(--ink);overflow:hidden;}

  .usage{position:absolute;left:52px;top:8px;width:298px;font-size:11.6px;line-height:1.36;}
  .usage h3{color:var(--teal);font-size:11.6px;font-weight:700;}
  .usage p{margin-bottom:9px;text-align:justify;}
  .usage .warn-head{font-weight:700;font-size:13px;margin-top:2px;}
  .usage .warn{font-weight:700;font-size:10.6px;line-height:1.45;}
  .disclaimer{position:absolute;left:52px;top:237px;width:298px;border:1px solid var(--ink);padding:3px 6px;font-size:11.6px;line-height:1.35;}

  .brand{position:absolute;left:398px;top:40px;width:220px;text-align:center;}
  .brand-dot{width:30px;height:30px;border-radius:50%;background:var(--green);margin:0 auto 8px;}
  .brand-name{font-family:"Open Sans",sans-serif;font-weight:700;color:var(--green);font-size:22px;line-height:1.1;letter-spacing:1px;}

  .title-bar{position:absolute;left:430px;top:157px;width:346px;height:52px;background:var(--teal);display:flex;align-items:center;justify-content:center;}
  .title-bar h1{font-family:"Syncopate",sans-serif;color:var(--white);font-size:28px;font-weight:700;letter-spacing:0;}
  .potency{position:absolute;left:348px;top:218px;width:510px;text-align:center;font-family:"Archivo Black",sans-serif;font-size:31px;letter-spacing:3px;}
  .tech{position:absolute;left:348px;top:257px;width:510px;text-align:center;font-family:"Roboto Condensed",sans-serif;font-size:20px;}
  .tech b{font-weight:700;}

  .decor{position:absolute;left:790px;top:20px;width:140px;height:260px;background:radial-gradient(ellipse at center,rgba(35,160,147,.12),rgba(35,160,147,0) 70%);}

  .facts{position:absolute;left:940px;top:6px;width:240px;height:252px;border:1.5px solid var(--ink);padding:2px 7px;font-size:12px;}
  .facts h2{font-size:24px;font-weight:700;text-align:center;line-height:1.1;}
  .facts .serving{font-weight:700;font-size:13px;padding-left:26px;border-bottom:5px solid var(--ink);padding-bottom:2px;}
  .facts .amount{text-align:right;font-weight:700;font-size:11px;border-bottom:1px solid var(--ink);padding:2px 0;}
  .facts .blend{display:grid;grid-template-columns:1fr 86px 14px;border-bottom:2px solid var(--ink);padding:3px 0 3px;line-height:1.1;}
  .facts .blend small{grid-column:1/4;font-size:10px;margin-top:2px;}
  .facts .strains{display:grid;grid-template-columns:146px 1fr;padding:4px 0 3px;line-height:1.22;border-bottom:2px solid var(--ink);}
  .facts .note{padding-top:3px;}
  .other{position:absolute;left:940px;top:260px;width:250px;font-size:11.4px;line-height:1.4;}
  .other b{font-weight:700;}

  .band{position:absolute;left:0;top:296px;width:1200px;height:82px;background:linear-gradient(90deg,var(--green),var(--green-light),var(--green));}
  .band-note{position:absolute;left:60px;top:306px;width:276px;height:54px;background:var(--green-light);color:var(--white);font-size:11.4px;line-height:1.3;padding:3px 8px;}
  .count{position:absolute;left:425px;top:286px;width:66px;height:86px;background:var(--teal);border:3px solid var(--white);color:var(--white);text-align:center;}
  .count strong{display:block;font-family:"Archivo Black",sans-serif;font-size:26px;line-height:1.25;margin-top:10px;}
  .count span{font-size:12px;font-weight:700;}
  .photo{position:absolute;top:296px;width:68px;height:74px;}
  .photo-1{left:497px;background:linear-gradient(135deg,#5fb3d8,#1b6fa3);}
  .photo-2{left:592px;background:linear-gradient(135deg,#d7efe6,#7ec9a2);}
  .photo-3{left:688px;background:linear-gradient(135deg,#3a79c4,#c8424f);}

  .footer{position:absolute;left:0;top:378px;width:1200px;height:67px;background:var(--teal);color:var(--white);}
  .distributor{position:absolute;left:60px;top:2px;font-size:13px;line-height:1.25;}
  .distributor b{font-weight:700;}
  .badges{position:absolute;left:960px;top:4px;display:flex;gap:20px;}
  .badge{width:40px;height:34px;background:var(--white);opacity:.9;}
  .badge.round{border-radius:50%;width:34px;}
  .lot{position:absolute;left:945px;top:47px;font-size:11px;}
</style>
</head>
<body>
<div class="label">
  <section class="usage">
    <h3>Suggested use:</h3>
    <p>As a dietary supplement, take two (2) capsules once daily. For best results, take one (1) capsule during the day and one (1) capsule in the evening. Repeat the process daily. Do not exceed two capsules per day.</p>
    <p>Floriva-40 offers a balanced spectrum of live organisms. Probiotic bacteria are critical for healthy digestion, help maintain the integrity of the intestinal lining, support proper intestinal motility and participate in the detoxification process.*</p>
    <div class="warn-head">KEEP OUT OF REACH OF CHILDREN.</div>
    <div class="warn">DO NOT USE IF SAFETY SEAL IS DAMAGED OR MISSING.<br>STORE IN A COOL DRY PLACE.</div>
  </section>
  <div class="disclaimer">*These statements have not been evaluated by the Food and Drug Administration. This product is not intended to diagnose, treat,cure or prevent any disease.</div>

  <div class="brand">
    <div class="brand-dot"></div>
    <div class="brand-name">HARVEST ROOT<br>LABS</div>
  </div>

  <div class="title-bar"><h1>FLORIVA-40</h1></div>
  <div class="potency">40 BILLION CFU</div>
  <div class="tech"><b>VELTRA ®</b> Bi-Pass Technology</div>

  <div class="decor" role="img" aria-label="Scattered light teal cross decoration"></div>

  <section class="facts">
    <h2>Supplement Facts:</h2>
    <div class="serving">Serving size: &nbsp;2 Capsules</div>
    <div class="amount">Amount Per Serving %DV</div>
    <div class="blend"><span>Proprietary Blend of<br>Probiotic Bacteria:</span><span>40 Billion CFU</span><span>**</span><small>VELTRA® (Bi-Pass Technology)</small></div>
    <div class="strains">
      <span>Lactobacillus acidophilus</span><span>(KW-14)</span>
      <span>Bifidobacterium lactis</span><span>(KW-04)</span>
      <span>Lactobacillus plantarum</span><span>(KW-115)</span>
      <span>Lactobacillus paracasei</span><span>(KW-37)</span>
      <span>Marine Polysaccharide Complex</span><span></span>
      <span>Fructooligosaccharide</span><span></span>
    </div>
    <div class="note">** Daily Value (DV) not established</div>
  </section>
  <div class="other"><b>Other Ingredients:</b> Cellulose (Vegetable Capsule).<br>Rice maltodextrin, L-Leucine</div>

  <div class="band" role="img" aria-label="Green diamond pattern band"></div>
  <div class="band-note">This product is formulated with 40 billion CFU per 2 capsules, to deliver a minimum potency of 20 billion CFU per 2 capsules through the best by date.</div>
  <div class="count"><strong>30</strong><span>capsules</span></div>
  <div class="photo photo-1" role="img" aria-label="Microscope view of blue probiotic bacteria"></div>
  <div class="photo photo-2" role="img" aria-label="Laboratory glassware with green liquid"></div>
  <div class="photo photo-3" role="img" aria-label="Microscope view of red and blue gut bacteria"></div>

  <footer class="footer">
    <div class="distributor"><b>Distributed By:</b> Company Name<br>Address, City, ST Zip Code<br>website &amp; contact details</div>
    <div class="badges">
      <div class="badge"></div>
      <div class="badge"></div>
      <div class="badge round"></div>
      <div class="badge"></div>
    </div>
    <div class="lot">Lot no. &amp; Expiration Date printed on bottom of bottle</div>
  </footer>
</div>
</body>
</html>
```